Chairside Roots: the dental helper's field guide, start to finish

Book cover:

Book about dental implantology
Reader is a dental assistant
Introduction to surgical knowledge to case acceptance. We will start with the intro to implants that will cover population stats on tooth loss, how to make the patient trust the team, how to communicate with the patient. Then we will get more technical; bone loss, bone quality and quantity. We will also inform on pros and cons of different classic dental treatments vs implant treatment. Surgical knowledge deep into various aspects of implants procedures. An illustration of surgical instruments needed and motors and hand pieces. Operatory set up will be demonstrated. I’ll be guiding the role of the surgical assistant and non surgical assistant. At the end I’ll explain how to close an implant case. From single implants to more complex cases.

Target Market(s)

Dental assistants

Industry/Entity Type

Dental

Font styles to use
Other font styles liked:
• Mellifluous or addington

Colors
EE7325
F08F49
F5BC92
FAE3D3
FDF4ED

Requirements
Must have
• Dental implant, positive vibe, orange Colors, professional
Nice to have
• Sense of team spirit, uncluttered,
Should not have
• Images of people

```html
<!DOCTYPE html>
<html lang="en">
<head>
<meta charset="utf-8">
<title>Dental Implantology – Book Cover Spread</title>
<link href="https://fonts.googleapis.com/css2?family=Merriweather:wght@700;900&family=Tinos:wght@400;700&display=swap" rel="stylesheet">
<style>
  :root{
    --orange:#ef5a24;
    --orange-title:#e4532a;
    --orange-soft:#f08f49;
    --peach:#f5bc92;
    --peach-light:#fae3d3;
    --cream:#fdf4ed;
    --paper:#ffffff;
    --ink:#2b2b2b;
    --steel-light:#eef0f2;
    --steel-mid:#d3d6da;
    --steel-dark:#a9aeb4;
    --bg:#ffffff;
  }
  *{box-sizing:border-box;margin:0;padding:0}
  html,body{width:840px;height:1200px;overflow:hidden;background:var(--bg)}
  .canvas{position:relative;width:840px;height:1200px}
  .spread{
    position:absolute;left:16px;top:304px;width:808px;height:591px;
    display:flex;border:1px solid var(--orange);background:var(--paper);
  }
  .back-cover,.front-cover{position:relative;width:393px;height:100%;overflow:hidden}
  .spine{
    position:relative;width:22px;height:100%;
    border-left:1px solid var(--orange);border-right:1px solid var(--orange);
  }
  .spine-text{
    writing-mode:vertical-rl;
    font-family:"Merriweather",Georgia,serif;font-weight:700;
    font-size:10px;color:var(--orange-title);letter-spacing:.3px;
    position:absolute;left:50%;transform:translateX(-50%);
  }
  .spine-title{top:86px}
  .spine-tagline{top:345px;font-family:"Tinos","Times New Roman",serif;font-weight:400}

  .title{
    position:absolute;left:0;right:0;text-align:center;top:92px;
    font-family:"Merriweather",Georgia,serif;font-weight:900;
    font-size:24px;color:var(--orange-title);letter-spacing:.2px;
  }
  .back-subtitle{
    position:absolute;top:128px;left:0;right:0;text-align:center;
    font-family:"Tinos","Times New Roman",serif;font-size:11.5px;color:var(--orange);
  }
  .blurb{
    position:absolute;top:194px;left:28px;width:337px;
    font-family:"Tinos","Times New Roman",serif;font-size:10.6px;line-height:13.1px;
    color:var(--ink);text-align:justify;
  }
  .pattern{position:absolute;left:0;right:0}
  .pattern-back{bottom:0;height:150px;
    background:linear-gradient(180deg,rgba(250,227,211,0),var(--peach-light) 70%,var(--peach-light))}
  .pattern-front{top:0;height:92px;
    background:linear-gradient(180deg,var(--peach-light),var(--cream) 75%,rgba(253,244,237,0))}

  .author{
    position:absolute;left:0;right:0;text-align:center;
    font-family:"Tinos","Times New Roman",serif;font-size:23px;color:var(--orange);letter-spacing:.3px;
  }
  .back-cover .author{bottom:10px}
  .front-cover .author{top:469px}

  .front-subtitle{
    position:absolute;top:142px;left:0;right:0;text-align:center;
    font-family:"Merriweather",Georgia,serif;font-weight:700;font-size:9.5px;color:var(--orange-title);
  }
  .illustration{
    position:absolute;top:181px;left:25px;width:332px;height:262px;border-radius:8px;
    background:linear-gradient(155deg,var(--steel-light) 0%,var(--steel-light) 30%,var(--steel-mid) 65%,var(--steel-dark) 100%);
  }
  .feature-line{
    position:absolute;top:238px;left:36px;
    font-family:"Merriweather",Georgia,serif;font-weight:700;font-size:10px;line-height:19px;color:var(--orange-title);
  }
  .tagline-band{
    position:absolute;left:0;right:0;bottom:0;height:65px;background:var(--orange);
    display:flex;align-items:center;justify-content:center;
    font-family:"Tinos","Times New Roman",serif;font-size:23px;color:#fff;letter-spacing:.4px;
  }
</style>
</head>
<body>
<main class="canvas">
  <section class="spread">
    <article class="back-cover">
      <div class="pattern pattern-back" role="img" aria-label="Soft peach and orange triangle mosaic pattern fading upward"></div>
      <h2 class="title">DENTAL IMPLANTOLOGY</h2>
      <p class="back-subtitle">Chairside Roots: the dental helper's field guide, start to finish</p>
      <p class="blurb">Lorem ipsum dolor sit amet, consectetuer adipiscing elit, sed diam nonummy nibh euismod tincidunt ut laoreet dolore magna aliquam erat volutpat. Ut wisi enim ad minim veniam, quis nostrud exerci tation ullamcorper suscipit lobortis nisl ut aliquip ex ea commodo consequat. Duis autem vel Lorem ipsum dolor sit amet, consectetuer adipiscing elit, sed diam nonummy nibh euismod tincidunt ut laoreet dolore magna aliquam erat volutpat. Ut wisi enim ad minim veniam, quis nostrud exerci tation ullamcorper suscipit lobortis nisl ut aliquip ex ea commodo consequat. Duis autem vel Lorem ipsum dolor sit amet, consectetuer adipiscing elit, sed diam nonummy nibh euismod tincidunt ut laoreet dolore magna aliquam erat volutpat. Ut wisi enim ad minim veniam, quis nostrud exerci tation ullamcorper suscipit lobortis nisl ut aliquip ex ea commodo consequat. Duis autem vel Lorem ipsum dolor sit amet, consectetuer adipiscing elit, sed diam nonummy nibh euismod tincidunt ut laoreet dolore magna aliquam erat volutpat. Ut wisi enim ad minim veniam, quis nostrud exerci tation ullamcorper suscipit lobortis nisl ut aliquip ex ea commodo consequat. Duis autem vel Lorem ipsum dolor sit amet, consectetuer adipiscing elit, sed diam nonummy nibh euismod tincidunt ut laoreet dolore magna aliquam erat volutpat.</p>
      <p class="author">AUTHOR NAME</p>
    </article>

    <aside class="spine">
      <span class="spine-text spine-title">DENTAL IMPLANTOLOGY</span>
      <span class="spine-text spine-tagline">THE WAY TO EFFICIENCY</span>
    </aside>

    <article class="front-cover">
      <div class="pattern pattern-front" role="img" aria-label="Soft peach and orange triangle mosaic pattern across the top"></div>
      <h1 class="title">DENTAL IMPLANTOLOGY</h1>
      <p class="front-subtitle">"Dental Assistant's Comprehensive Guide to Implantology"</p>
      <div class="illustration" role="img" aria-label="Illustration of a natural tooth, a dental implant with crown, an exploded implant with abutment screw and crown, a dental probe and a mouth mirror"></div>
      <p class="feature-line">Essential Knowledge<br>and Skills for Dental<br>Assistants in Implantology</p>
      <p class="author">AUTHOR NAME</p>
      <div class="tagline-band">THE WAY TO EFFICIENCY</div>
    </article>
  </section>
</main>
</body>
</html>
```